Invitation card to the opening of BRISKORA FITNESS CLUB

A successful training plan starts with BRISKORA Fitness!
Join us for our grand opening! OPEN HOUSE AND YOU ARE INVITED!
Tuesday 1st of August, 2017
Classes start from 7.30am till 9.30pm.
Explore the most fun, exciting, challenging and effective training system in the region.
Healthy drinks and delicious food will be provided.
We hope to see you there!

www.briskorafitnessclub.example
APP: BRISKORAFITNAB
Tel: 71-42 58 19

Industry/Entity Type

Fitness

Colors

Designer to choose colors to be used in the design.

Requirements
Must have
• Elegant card
Nice to have
• Logo in the background
Should not have
• pictures

```html
<!DOCTYPE html>
<html lang="en">
<head>
<meta charset="utf-8">
<title>Briskora Fitness Club – Grand Opening Invitation</title>
<link rel="stylesheet" href="https://fonts.googleapis.com/css2?family=Archivo+Black&family=Arimo:wght@400;700&family=Cinzel:wght@400;600&family=Pinyon+Script&display=swap">
<style>
  :root {
    --stage: #2b2b2d;
    --navy: #0f3d57;
    --navy-deep: #0a2f45;
    --gold-light: #f6e7a8;
    --gold: #d9b65a;
    --gold-dark: #a37a26;
    --cream: #e9dcae;
    --ink: #111111;
    --white: #ffffff;
  }
  * { margin: 0; padding: 0; box-sizing: border-box; }
  html, body { width: 1200px; height: 750px; overflow: hidden; }
  body { background: var(--stage); position: relative; }

  .invitation {
    position: absolute; left: 340px; top: 10px;
    width: 520px; height: 730px;
    background: radial-gradient(ellipse at 50% 40%, #14506f 0%, var(--navy) 55%, var(--navy-deep) 100%);
    overflow: hidden;
  }
  .invitation__frame {
    position: absolute; inset: 8px;
    border: 1.5px solid var(--gold);
    pointer-events: none;
  }
  .corner-ornament {
    position: absolute; width: 86px; height: 66px;
    background: radial-gradient(circle at 20% 20%, var(--gold-light), var(--gold) 45%, transparent 75%);
    opacity: .9;
  }
  .corner-ornament--tl { left: 0; top: 0; }
  .corner-ornament--tr { right: 0; top: 0; transform: scaleX(-1); }
  .corner-ornament--bl { left: 0; bottom: 0; transform: scaleY(-1); }
  .corner-ornament--br { right: 0; bottom: 0; transform: scale(-1,-1); }

  .brand {
    position: absolute; top: 28px; left: 0; width: 100%;
    text-align: center; color: var(--white);
    font-family: "Cinzel", serif; font-weight: 400;
  }
  .brand__mark { display: block; margin: 0 auto 10px; }
  .brand__name { font-size: 54px; line-height: 1; letter-spacing: 1px; }
  .brand__sub { font-size: 20px; letter-spacing: 9px; margin-top: 6px; padding-left: 9px; }

  .headline-band {
    position: absolute; left: 0; top: 241px; width: 100%; height: 133px;
    background: linear-gradient(90deg, var(--gold-dark) 0%, var(--gold) 18%, var(--gold-light) 50%, var(--gold) 82%, var(--gold-dark) 100%);
    text-align: center; padding-top: 14px;
    font-family: "Archivo Black", "Arimo", sans-serif; text-transform: uppercase;
  }
  .headline-band__top { font-size: 36px; line-height: 1.05; color: var(--navy); letter-spacing: -0.5px; }
  .headline-band__mid { font-family: "Arimo", sans-serif; font-weight: 700; font-size: 27px; line-height: 1.1; color: var(--ink); }
  .headline-band__bottom { font-size: 33px; line-height: 1.1; color: var(--navy); }

  .invite {
    position: absolute; top: 386px; width: 100%; text-align: center;
    font-family: "Arimo", sans-serif; font-weight: 700; font-size: 18px; line-height: 29px;
    color: var(--cream);
  }
  .event-date {
    position: absolute; top: 448px; width: 100%; text-align: center;
    color: var(--cream); white-space: nowrap;
  }
  .event-date__script { font-family: "Pinyon Script", cursive; font-size: 36px; }
  .event-date__year { font-family: "Cinzel", serif; font-weight: 600; font-size: 34px; }

  .divider { position: absolute; height: 2px; background: var(--gold); }
  .divider--full { left: 0; right: 0; top: 513px; }
  .divider--short { left: 8px; width: 148px; top: 607px; }

  .details {
    position: absolute; top: 524px; width: 100%; text-align: center;
    font-family: "Arimo", sans-serif; font-size: 13.5px; line-height: 21px;
    color: var(--cream); text-transform: uppercase;
  }

  .hours-badge { position: absolute; left: 376px; top: 588px; width: 112px; height: 112px; }

  .contact {
    position: absolute; top: 674px; width: 100%; text-align: center;
    font-family: "Arimo", sans-serif; font-size: 14px; line-height: 22px; color: var(--cream);
  }
  .contact__sep { color: var(--gold); padding: 0 4px; }
</style>
</head>
<body>
  <article class="invitation">
    <div class="corner-ornament corner-ornament--tl" role="img" aria-label="Gold filigree corner ornament"></div>
    <div class="corner-ornament corner-ornament--tr" role="img" aria-label="Gold filigree corner ornament"></div>
    <div class="corner-ornament corner-ornament--bl" role="img" aria-label="Gold filigree corner ornament"></div>
    <div class="corner-ornament corner-ornament--br" role="img" aria-label="Gold filigree corner ornament"></div>
    <div class="invitation__frame"></div>

    <header class="brand">
      <svg class="brand__mark" width="92" height="92" viewBox="0 0 92 92" aria-hidden="true">
        <circle cx="46" cy="46" r="40" fill="none" stroke="#d0d4d8" stroke-width="7"/>
      </svg>
      <div class="brand__name">BRISKORA</div>
      <div class="brand__sub">FITNESS</div>
    </header>

    <section class="headline-band">
      <div class="headline-band__top">Successful Training</div>
      <div class="headline-band__mid">Plan Starts With</div>
      <div class="headline-band__bottom">Briskora Fitness!</div>
    </section>

    <p class="invite">Join Us For Our Grand Opening!<br>Open House And You Are Invited!</p>

    <p class="event-date">
      <span class="event-date__script">Tuesday 1st of August,</span>
      <span class="event-date__year">2017</span>
    </p>

    <div class="divider divider--full"></div>

    <p class="details">
      Explore the most fun, exciting, challenging<br>
      and effective trainingsystem in the region.<br>
      Healthy drinks and delicious food will be provided.<br>
      We hope to see you there!
    </p>
    <div class="divider divider--short"></div>

    <svg class="hours-badge" viewBox="0 0 112 112" role="img" aria-label="Classes start from 7.30am till 9.30pm">
      <defs>
        <radialGradient id="badgeGold" cx="40%" cy="35%" r="70%">
          <stop offset="0" stop-color="#fff4bf"/>
          <stop offset=".55" stop-color="#e3c063"/>
          <stop offset="1" stop-color="#a37a26"/>
        </radialGradient>
      </defs>
      <polygon fill="url(#badgeGold)" points="56,2 63,14 75,5 78,19 92,15 90,29 104,30 97,42 110,48 100,57 110,66 97,71 104,83 90,84 92,98 78,94 75,108 63,99 56,110 49,99 37,108 34,94 20,98 22,84 8,83 15,71 2,66 12,57 2,48 15,42 8,30 22,29 20,15 34,19 37,5 49,14"/>
      <g font-family="Arimo, sans-serif" font-weight="700" fill="#111" text-anchor="middle" transform="rotate(-22 56 56)">
        <text x="56" y="38" font-size="11">Classes start</text>
        <text x="56" y="50" font-size="10">from</text>
        <text x="56" y="66" font-size="17">7.30am</text>
        <text x="56" y="77" font-size="10">till</text>
        <text x="56" y="93" font-size="17">9.30pm</text>
      </g>
    </svg>

    <footer class="contact">
      briskorafitnab <span class="contact__sep">|</span>71-42 58 19<br>
      www.briskorafitnessclub.example
    </footer>
  </article>
</body>
</html>
```